THE KINDLING LANTERN

project description

The Kindling Lantern was created to challenge the lack of meaning and values in power of mainstream media.

This website will be a platform through which you can explore the meaning of humanity, through a variety of lenses - philosophy, politics, science, art, human interest stories, etc.

As an organization, TKL aims to further the understanding of the meaning of humanity, including its spiritual and existential challenges in 21st century. We wish to inspire and develop this understanding, while transforming mass media and “visual” spaces so they display the beauty and interconnectedness of human beings.

We believe that The Kindling Lantern and that our “visual” space and mass media should reflect and support those values.

We are looking to create an image that may be seen on the site independently, full screen - or as the background to the home page (with text on top of it, potentially.)
Updates

 

 The city/the background with the advertisementshouldn’t be to depressing because (indigo blue or light gray color) so overall, the page has a pleasant soft look and feel.

 

Also place the boy is looking at needs to have advertisement

 

Thank you

Target Market(s)

people that are sophisticated, modern, engage, care, awere, who are interested scholarly discussions of media, philosophy,art/desighn community - as well as the human spirit.

Industry/Entity Type

Media

Requirements
Must have
• I have photos of a boy looking up. I would like to take this image (pick one) and incorporate into a city scene - one with buildings littered with mass media information and adds - similar to the look of NYC's Wexford Plaza. He is looking up a bit overwhelmed trying to make sense of the world he is seeing.
Nice to have
• However, the city scene in the background may be sketched or distorted
Should not have
• should not be agresive or too busy

```html
<!DOCTYPE html>
<html lang="en">
<head>
<meta charset="utf-8">
<title>The Kindling Lantern</title>
<link rel="stylesheet" href="https://fonts.googleapis.com/css2?family=Arimo:wght@400;700&display=swap">
<style>
:root{
  --topbar:#1d1d1d;
  --header-light:#ffffff;
  --header-dark:#dcdcdc;
  --ink:#222222;
  --muted:#666666;
  --rule:#dddddd;
  --blue:#2a7fc9;
  --blue-dark:#1b63a6;
  --blue-light:#4aa3e6;
  --link:#1a75c4;
  --band:#1c1c1c;
  --footer:#262626;
  --footer-text:#6e6e6e;
  --footer-head:#e0e0e0;
}
*{box-sizing:border-box;margin:0;padding:0}
html,body{width:1047px;height:1200px;overflow:hidden}
body{font-family:'Arimo',Arial,sans-serif;background:#fff;color:var(--ink);position:relative}
.abs{position:absolute}

.topbar{left:0;top:0;width:1047px;height:20px;background:var(--topbar);color:#ccc;font-size:9px;line-height:20px}
.topbar .find{left:109px}
.social{left:170px;top:5px;display:flex;gap:6px}
.social span{width:10px;height:10px;border-radius:2px;background:var(--blue-light)}
.social span:last-child{background:#e8872b}
.topbar .support{right:120px}
.topbar .support b{color:var(--blue-light);font-weight:400}

.header{left:0;top:20px;width:1047px;height:566px;background:radial-gradient(ellipse at 50% 30%,var(--header-light) 0%,#f2f2f2 45%,var(--header-dark) 100%)}
.brand{left:0;top:28px;width:1047px;text-align:center;font-weight:700;font-size:18px;letter-spacing:-0.3px;color:#333}
.brand .dot{display:inline-block;width:9px;height:9px;border-radius:50%;background:#333;margin:0 6px 2px}
.brand-sub{left:0;top:51px;width:1047px;text-align:center;font-size:8px;color:#888;letter-spacing:.5px}

.nav{left:121px;top:103px;width:804px;height:37px;border-radius:18px;background:linear-gradient(#fdfdfd,#e9e9e9);box-shadow:0 1px 3px rgba(0,0,0,.15)}
.nav a{position:absolute;top:11px;font-size:10.5px;color:#333;text-decoration:none}
.nav .active{left:11px;top:7px;width:91px;height:24px;line-height:24px;text-align:center;border-radius:6px;background:linear-gradient(var(--blue-light),var(--blue-dark));color:#fff}
.search{left:594px;top:7px;width:200px;height:24px;border:1px solid #ccc;border-radius:5px;background:#fff;overflow:hidden}
.search span{position:absolute;right:0;top:0;width:40px;height:24px;line-height:24px;text-align:center;background:linear-gradient(var(--blue-light),var(--blue-dark));color:#fff;font-size:10px}

.hero{left:112px;top:177px;width:822px;height:341px;background:linear-gradient(100deg,#b8324a 0%,#3a2a4e 30%,#1b1d3a 50%,#6a3a6e 70%,#e2a23a 100%)}
.hero-shadow{left:140px;top:518px;width:766px;height:28px;border-radius:50%;background:radial-gradient(ellipse at 50% 0%,rgba(0,0,0,.55),rgba(0,0,0,0) 70%)}

.feature{width:242px}
.feature h2{font-size:12px;font-weight:700;color:#111}
.feature .lead{font-size:8.5px;color:var(--muted);margin-top:3px;padding-bottom:8px;border-bottom:1px solid var(--rule)}
.thumb{margin-top:10px;height:85px;border:1px solid #e3e3e3;padding:3px}
.thumb div{width:100%;height:100%;display:flex;align-items:center;justify-content:center;font-size:16px}
.body{margin-top:12px;font-size:8.5px;line-height:17px;color:#444}
.body a{color:var(--link)}
.btn{display:inline-block;margin-top:8px;height:18px;line-height:18px;padding:0 8px;border-radius:3px;background:linear-gradient(var(--blue-light),var(--blue-dark));color:#fff;font-size:8px}

.band{left:0;top:934px;width:1047px;height:56px;background:var(--band)}
.band .msg{left:112px;top:13px;font-size:10px;color:var(--blue-light)}
.band .sub{left:112px;top:27px;font-size:8px;color:#777}
.band .cta{left:790px;top:10px;width:138px;height:34px;line-height:34px;text-align:center;border-radius:4px;background:linear-gradient(var(--blue-light),var(--blue-dark));color:#111;font-size:14px}

.footer{left:0;top:990px;width:1047px;height:210px;background:var(--footer)}
.fcol{top:22px}
.fcol h3{font-size:12px;color:var(--footer-head);font-weight:700;margin-bottom:14px}
.fcol p{font-size:8.5px;color:var(--footer-text);line-height:17px}
.frule{left:112px;top:160px;width:822px;height:1px;background:#3a3a3a}
.copy{left:112px;top:176px;font-size:8.5px;color:#999}
.copy b{color:#ddd;font-weight:700}
</style>
</head>
<body>

<div class="abs topbar">
  <span class="abs find">Find us on:</span>
  <div class="abs social"><span></span><span></span><span></span><span></span><span></span></div>
  <span class="abs support">Click here to live Support &nbsp;Toll Free <b>1-800-555-0142</b></span>
</div>

<div class="abs header">
  <div class="abs brand"><span class="dot"></span>THE KINDLING LANTERN<span class="dot"></span></div>
  <div class="abs brand-sub">ORGANIZATION</div>
</div>

<nav class="abs nav">
  <a class="active" href="#">Home</a>
  <a href="#" style="left:128px">Services</a>
  <a href="#" style="left:227px">Media</a>
  <a href="#" style="left:300px">About Us</a>
  <a href="#" style="left:389px">Contact Us</a>
  <div class="abs search"><span>Go</span></div>
</nav>

<div class="abs hero" role="img" aria-label="Night city plaza covered in glowing billboards, a boy looking up at the signs"></div>
<div class="abs hero-shadow"></div>

<section class="abs feature" style="left:112px;top:632px">
  <h2>Interface development</h2>
  <p class="lead">Lorem ipsum dolor sit amet, consectetur adipiscing elit</p>
  <div class="thumb"><div role="img" aria-label="Lantern Web banner" style="background:linear-gradient(90deg,#fff 40%,#f3c2dc)">Lantern Web</div></div>
  <p class="body"><a>Lorem ipsum dolor sit amet</a>, consectetur adipiscing elit, sed do eiusmod tempor incididunt ut labore et dolore magna aliqua. Ut enim ad minim veniam, quisnostrud exercitation ullamco laboris nisi ut aliquip.</p>
  <span class="btn">Read More »</span>
</section>

<section class="abs feature" style="left:400px;top:632px">
  <h2>Design and Marketing</h2>
  <p class="lead">Lorem ipsum dolor sit amet, consectetur adipiscing elit</p>
  <div class="thumb"><div role="img" aria-label="Lantern Studio banner" style="background:linear-gradient(90deg,#5a0f22,#c8244e);color:#fff">Lantern Studio</div></div>
  <p class="body">Lorem ipsum dolor sit amet, consectetur adipiscing elit. Integer ante nibh, ultrices et rhoncus et, viverra eget ante. <a>Mauris interdum velit lacus</a>, sit amet rutrum augue. Morbi sit amet viverra massa. Maecenas felis mi, lobortis ut elementum vitae, placerat a justo.</p>
  <span class="btn">Read More »</span>
</section>

<section class="abs feature" style="left:686px;top:632px">
  <h2>24h technical support</h2>
  <p class="lead">Lorem ipsum dolor sit amet, consectetur adipiscing elit</p>
  <div class="thumb"><div role="img" aria-label="Lantern Media banner" style="background:linear-gradient(90deg,#b3711c,#f2d38c);color:#fff">Lantern Media</div></div>
  <p class="body">Mauris interdum velit lacus, sit amet rutrum augue. Morbi sit amet viverra massa. Maecenas felis mi, lobortis ut elementum vitae, placerat a justo. Aliquam quis mauris justo. Curabitur vel dolor et quam imperdiet fermentum.</p>
  <span class="btn">Read More »</span>
</section>

<div class="abs band">
  <div class="abs msg">Your company's welcome message or slogan.</div>
  <div class="abs sub">Donec metus lacus, porta id, auctor sit amet, aliquet eu, lacus. Quisque sagittis vulputate orci.</div>
  <div class="abs cta">Contact Us</div>
</div>

<footer class="abs footer">
  <div class="abs fcol" style="left:112px"><h3>About</h3><p>Overview<br>Another Link<br>Our Company<br>Our Staff<br>Mission Statement</p></div>
  <div class="abs fcol" style="left:260px"><h3>Services</h3><p>First Service<br>Second Service<br>Another Service<br>A Fourth Service</p></div>
  <div class="abs fcol" style="left:411px"><h3>Media</h3><p>Image Gallery<br>Video Gallery<br>Audio Files<br>The Podcast</p></div>
  <div class="abs fcol" style="left:545px"><h3>Blog</h3><p>Category One<br>Category 2<br>Another Category<br>Category<br>A Fifth Category</p></div>
  <div class="abs fcol" style="left:692px"><h3>More Links</h3><p>Sign Up Now<br>We Are Hiring<br>Terms &amp; Conditions<br>Privacy Policy</p></div>
  <div class="abs fcol" style="left:834px"><h3>Contact Us</h3><p>Email Sales<br>Email Support<br>Phone: 555-014-2290<br>Send Us Feedback</p></div>
  <div class="abs frule"></div>
  <div class="abs copy">© Copyright The Kindling Lantern . All Rights Reserved. &nbsp;&nbsp;&nbsp; <b>Home</b> | <b>Contact</b> | <b>RSS</b></div>
</footer>

</body>
</html>
```